Educational video design for millenials

We have a Podcast marketing design already (included below) and want to design the structure of the educational videos we are about to record in the next week to match the Podcast name (Harbourline Dental hour) and create a professional, tech savvy style with other design features to be created as the bookends of 5-10 minute video vignettes The aim is to attract young Millenials looking for initially free podcasts and video vignettes to encourage them to become financial members which will unlock the services we have developed over 25 years of being leaders in clinical development.
The initial marketing will be to the Australian dental professionals (about 8,000) expanding to Aisa (over 20,000).
The podcast interview style will be with visiting specialists who are world leaders in their skills and we aim to make this site a platform for excellent freely available podcasts and short videos encouraging the development of memberships to the greater value areas.

Target Market(s)

Millenial dentists, digitally savvy, strong Asian base as well as Australian NZ

Industry/Entity Type

Dentistry specically digital online learning

Font styles to use
Serif

Requirements
Must have
• Digital tech savvy feel with prfoessional elegance
Nice to have
• Professional, tech savvy, appealing to millenials who want to learn the latest technology in digital and cosmetic dentistry

```html
<!DOCTYPE html>
<html lang="en">
<head>
<meta charset="utf-8">
<title>Harbourline Dental hour — Video Graphics Storyboard</title>
<link rel="stylesheet" href="https://fonts.googleapis.com/css2?family=Catamaran:wght@300;400;600;700&family=Arimo:wght@400;700&display=swap">
<style>
  :root {
    --page: #ffffff;
    --ink: #111111;
    --navy-deep: #030a3a;
    --navy: #071a6b;
    --navy-glow: #0d2fa8;
    --cyan: #22b8f0;
    --cyan-bright: #41d6ff;
    --violet: #4a43c9;
    --tooth: #e9eef5;
    --black-panel: #101010;
    --light-panel: #f6f7f9;
    --ring-grey: #4f5568;
    --white: #ffffff;
  }
  * { box-sizing: border-box; margin: 0; padding: 0; }
  html, body { width: 1179px; height: 1200px; overflow: hidden; background: var(--page); }
  body { position: relative; font-family: "Catamaran", sans-serif; color: var(--ink); }

  .frame { position: absolute; width: 371px; height: 209px; overflow: hidden; }
  .col-1 { left: 22px; } .col-2 { left: 404px; } .col-3 { left: 786px; }
  .row-1 { top: 22px; } .row-2 { top: 292px; } .row-3 { top: 564px; } .row-4 { top: 838px; }

  .frame--space {
    background:
      radial-gradient(circle at 50% 45%, var(--navy-glow) 0%, var(--navy) 35%, var(--navy-deep) 100%);
  }
  .frame--black { background: var(--black-panel); }
  .frame--light { background: var(--light-panel); box-shadow: 0 3px 6px rgba(0,0,0,.18); }

  .facets { position: absolute; inset: 0; width: 100%; height: 100%; }

  .section-label {
    position: absolute; left: 0; width: 1179px; text-align: center;
    font-size: 23px; font-weight: 400; letter-spacing: .2px; line-height: 1;
  }

  .art { position: absolute; }
  .art--globe { left: 170px; top: 85px; width: 32px; height: 32px; border-radius: 50%;
    background: radial-gradient(circle at 70% 45%, #ffe7cf 0%, var(--cyan) 35%, #0a3fc0 100%); }
  .art--tooth-hero { left: 140px; top: 38px; width: 92px; height: 92px; border-radius: 50%;
    background: radial-gradient(circle at 45% 40%, var(--cyan-bright) 0%, #1a6fe6 45%, rgba(7,26,107,0) 75%); }

  .brand-title {
    position: absolute; left: 0; width: 100%; text-align: center;
    font-family: "Catamaran", sans-serif; font-weight: 600; color: var(--white);
    font-size: 17px; line-height: 1; letter-spacing: .2px;
  }

  .art--tooth-float { left: 74px; top: 72px; width: 44px; height: 56px; border-radius: 40% 40% 30% 30%;
    background: radial-gradient(circle at 45% 35%, var(--white) 0%, var(--tooth) 60%, #9aa7c2 100%); }
  .art--plinth { left: 48px; top: 158px; width: 92px; height: 34px; border-radius: 50%;
    background: radial-gradient(ellipse at 50% 40%, #5a55e0 0%, var(--violet) 70%, #2f2a9a 100%); }
  .art--dental-scene { left: 0; top: 40px; width: 180px; height: 150px; border-radius: 46% 54% 40% 60%;
    background: radial-gradient(ellipse at 50% 45%, #eef2f8 0%, #c9d2e3 35%, var(--violet) 70%, rgba(7,26,107,0) 100%); }

  .fact { position: absolute; left: 204px; top: 72px; width: 150px; color: var(--white); }
  .fact__title { font-size: 18px; font-weight: 700; line-height: 1; margin-bottom: 8px; }
  .fact__body { font-size: 7.8px; font-weight: 400; line-height: 1.3; }

  .placeholder-note {
    position: absolute; left: 0; top: 78px; width: 100%; text-align: center;
    color: #e6e6e6; font-weight: 300; font-size: 11px; letter-spacing: .6px; line-height: 1.55;
  }

  .lower-third { position: absolute; top: 150px; }
  .lower-third--left { left: 34px; text-align: left; }
  .lower-third--right { right: 38px; text-align: right; }
  .lower-third__name { display: block; color: var(--white); font-size: 15px; font-weight: 600; line-height: 1; margin-bottom: 2px; }
  .lower-third__role { display: inline-block; background: var(--cyan); color: var(--white); font-size: 9px; padding: 1px 5px; line-height: 1.2; }
  .lower-third__accent { position: absolute; width: 40px; height: 34px; top: -14px; }
  .lower-third--left .lower-third__accent { left: -4px; }
  .lower-third--right .lower-third__accent { right: -12px; }

  .rings { position: absolute; inset: 0; width: 100%; height: 100%; }

  .badge-disc { position: absolute; left: 113px; top: 31px; width: 145px; height: 145px; border-radius: 50%;
    background: radial-gradient(circle at 50% 45%, #0d1f78 0%, var(--navy-deep) 75%); border: 1px solid #1e3fbf; overflow: hidden; }
  .badge-disc .art--tooth-hero { left: 30px; top: 6px; width: 70px; height: 70px; }
  .badge-disc .brand-title { top: 90px; font-size: 13.5px; padding: 0 12px; line-height: 1.1; }

  .preview-link {
    position: absolute; left: 0; top: 1136px; width: 1179px; text-align: center;
    font-family: "Arimo", sans-serif; font-size: 25px; letter-spacing: .3px; color: var(--ink);
  }
  .preview-link strong { font-weight: 700; }
</style>
</head>
<body>

<!-- 01 Opening graphic -->
<section class="frame frame--space row-1 col-1">
  <svg class="facets" viewBox="0 0 371 209" aria-hidden="true">
    <polygon points="50,120 85,150 60,190" fill="#0b2a9a" opacity=".35"/>
    <polygon points="310,0 350,20 330,60" fill="#0b2a9a" opacity=".3"/>
    <line x1="215" y1="95" x2="250" y2="60" stroke="#3b6cff" stroke-width="1" opacity=".5"/>
  </svg>
  <div class="art art--globe" role="img" aria-label="Small glowing globe with lens flare"></div>
</section>

<section class="frame frame--space row-1 col-2">
  <svg class="facets" viewBox="0 0 371 209" aria-hidden="true">
    <polygon points="45,125 85,150 60,195" fill="#0b2a9a" opacity=".35"/>
    <polygon points="315,0 355,25 335,65" fill="#0b2a9a" opacity=".3"/>
  </svg>
  <div class="art art--tooth-hero" style="left:132px;top:32px;width:110px;height:100px" role="img" aria-label="Glowing wireframe tooth over a globe with lens flare"></div>
  <p class="brand-title" style="top:120px">Harbourline Dental hour</p>
</section>

<section class="frame frame--space row-1 col-3">
  <svg class="facets" viewBox="0 0 371 209" aria-hidden="true">
    <polygon points="45,125 85,150 60,195" fill="#0b2a9a" opacity=".35"/>
    <polygon points="315,0 355,25 335,65" fill="#0b2a9a" opacity=".3"/>
  </svg>
  <div class="art art--tooth-hero" style="left:132px;top:22px;width:110px;height:100px" role="img" aria-label="Glowing wireframe tooth over a globe with lens flare"></div>
  <p class="brand-title" style="top:128px;font-size:20px">Harbourline Dental hour</p>
</section>

<h2 class="section-label" style="top:242px">01 OPENING GRAPHIC</h2>

<!-- 02 Infographic / explainer -->
<section class="frame frame--space row-2 col-1">
  <svg class="facets" viewBox="0 0 371 209" aria-hidden="true">
    <polygon points="300,0 340,15 330,50" fill="#0b2a9a" opacity=".35"/>
    <polygon points="240,100 300,140 260,180" fill="#0b2a9a" opacity=".25"/>
  </svg>
  <div class="art art--tooth-float" role="img" aria-label="White 3D tooth floating"></div>
  <div class="art art--plinth" role="img" aria-label="Violet round plinth"></div>
</section>

<section class="frame frame--space row-2 col-2">
  <div class="art art--dental-scene" role="img" aria-label="3D tooth on a violet plinth with toothbrush, magnifier and dental probe"></div>
  <div class="fact">
    <h3 class="fact__title">Did you know?</h3>
    <p class="fact__body">Lorem ipsum dolor sit amet, consectetuer adipiscing elit, sed diam nonummy nibh euismod tinci</p>
  </div>
</section>

<section class="frame frame--space row-2 col-3">
  <div class="art art--dental-scene" role="img" aria-label="3D tooth on a violet plinth with toothbrush, magnifier and dental probe"></div>
  <div class="fact">
    <h3 class="fact__title">Did you know?</h3>
    <p class="fact__body">Lorem ipsum dolor sit amet, consectetuer adipiscing elit, sed diam nonummy nibh euismod tincidunt ut laoreet dolore magna aliquam erat volutpat.</p>
  </div>
</section>

<h2 class="section-label" style="top:512px">02 INFOGRAPHIC/EXPLAINER GRAPHIC</h2>

<!-- 03 Interview section / lower third -->
<section class="frame frame--black row-3 col-1">
  <p class="placeholder-note">TRANSPARENT BACKGROUND<br>[ INTERVIEW SECTION ]</p>
  <div class="lower-third lower-third--left">
    <svg class="lower-third__accent" viewBox="0 0 40 34" aria-hidden="true"><polygon points="4,16 26,0 20,34" fill="#1c5fd6" opacity=".7"/></svg>
    <span class="lower-third__name">Full Name</span>
    <span class="lower-third__role">Title/Expertise</span>
  </div>
</section>

<section class="frame frame--black row-3 col-2">
  <p class="placeholder-note">TRANSPARENT BACKGROUND<br>[ INTERVIEW SECTION ]</p>
  <div class="lower-third lower-third--right">
    <svg class="lower-third__accent" viewBox="0 0 40 34" aria-hidden="true"><polygon points="10,0 36,20 20,34" fill="#1c5fd6" opacity=".7"/></svg>
    <span class="lower-third__name">Full Name</span>
    <span class="lower-third__role">Title/Expertise</span>
  </div>
</section>

<section class="frame frame--black row-3 col-3">
  <p class="placeholder-note">TRANSPARENT BACKGROUND<br>[ INTERVIEW SECTION ]</p>
  <svg class="rings" viewBox="0 0 371 209" aria-hidden="true">
    <path d="M 340 160 A 150 150 0 0 0 280 -10" fill="none" stroke="#e4e6ea" stroke-width="44"/>
    <path d="M 60 230 A 150 150 0 0 1 20 120" fill="none" stroke="#d8dbe0" stroke-width="40" opacity=".9"/>
    <path d="M 270 160 A 110 110 0 0 1 170 225" fill="none" stroke="#e9ebee" stroke-width="30"/>
    <path d="M 115 50 A 80 80 0 0 0 105 125" fill="none" stroke="#e6e8eb" stroke-width="16"/>
    <path d="M 186 52 A 60 60 0 0 1 212 60" fill="none" stroke="#e6e8eb" stroke-width="14"/>
  </svg>
  <div class="lower-third lower-third--right">
    <span class="lower-third__name">Full Name</span>
    <span class="lower-third__role">Title/Expertise</span>
  </div>
</section>

<h2 class="section-label" style="top:786px">03 INTERVIEW SECTION/LOWER THIRD NAME</h2>

<!-- 04 End tag -->
<section class="frame frame--light row-4 col-1">
  <svg class="rings" viewBox="0 0 371 209" aria-hidden="true">
    <circle cx="185" cy="105" r="160" fill="none" stroke="#eceef2" stroke-width="40"/>
    <circle cx="185" cy="105" r="95" fill="none" stroke="#f0f1f4" stroke-width="30"/>
    <path d="M 110 105 A 75 75 0 0 1 192 30" fill="none" stroke="var(--ring-grey)" stroke-width="28"/>
    <path d="M 112 120 A 75 75 0 0 0 160 175" fill="none" stroke="var(--ring-grey)" stroke-width="28"/>
    <path d="M 258 120 A 75 75 0 0 1 235 185" fill="none" stroke="var(--ring-grey)" stroke-width="28"/>
    <circle cx="185" cy="105" r="36" fill="#0e1448"/>
  </svg>
</section>

<section class="frame frame--light row-4 col-2">
  <div class="badge-disc">
    <div class="art art--tooth-hero" style="left:30px;top:14px;width:90px;height:90px" role="img" aria-label="Glowing wireframe tooth over a globe with lens flare"></div>
  </div>
</section>

<section class="frame frame--light row-4 col-3">
  <div class="badge-disc">
    <div class="art art--tooth-hero" role="img" aria-label="Glowing wireframe tooth over a globe with lens flare"></div>
    <p class="brand-title">Harbourline Dental hour</p>
  </div>
</section>

<h2 class="section-label" style="top:1060px">04 ENDTAG - CAN BE INCLUDING SOCMED INFO</h2>

<p class="preview-link">VIDEO/MOTION PREVIEW LINK <strong>share.harbourpreview.net/t-8KqL2</strong></p>

</body>
</html>
```